College presentation for a startup bootcamp - how to talk to customers

I need a simple design for a college PowerPoint/ google slide presentation for students that are going through a Startup BootCamp. No flashy colors
- Accessible font - or provide the font - I like the tovra's website font or normal text font
- use a neutral colors schemes of grays - with 1-2 highlight colors
- You can use the photos in the presentation or others
- Urgent the presentation is on Thursday - I will award the winner on Wednesday.
- It's 23 slides long.

Target Market(s)

College students interested in startups

Industry/Entity Type

College

Font styles to use
Serif
Sans Serif
Other font styles liked:
• helvetica

Colors

Designer to choose only greyscale colors for use in the design.

Requirements
Must have
• clean , simple design neural colors like greyscale with 1-3 pop colors
Should not have
• no flashy colors, or hard to read text

```html
<!DOCTYPE html>
<html lang="en">
<head>
<meta charset="utf-8">
<title>Customer Development – How to talk to customers</title>
<link href="https://fonts.googleapis.com/css2?family=Source+Sans+3:ital,wght@0,400;0,600;0,700;1,400&display=swap" rel="stylesheet">
<style>
  :root {
    --board: #3f3f3f;
    --paper: #ffffff;
    --mist: #efeeec;
    --ink: #111111;
    --ink-soft: #333333;
    --rule: #9a9a9a;
    --panel-dark: #4a4846;
    --accent: #0e55a8;
    --alert: #d2452a;
  }
  * { box-sizing: border-box; margin: 0; padding: 0; }
  html, body { width: 1200px; height: 4187px; overflow: hidden; }
  body {
    background: var(--board);
    font-family: "Source Sans 3", "Helvetica Neue", Arial, sans-serif;
    color: var(--ink);
    position: relative;
  }
  .slide {
    position: absolute;
    left: 60px;
    width: 1098px;
    height: 616px;
    overflow: hidden;
    background: var(--mist);
  }
  .slide > * { position: absolute; }
  .brand { font-size: 25px; line-height: 30px; color: var(--ink); }
  .brand--light { color: #fff; }
  .photo { display: block; }
  .heading { font-size: 39px; line-height: 44px; font-weight: 700; }
  .heading .accent { color: var(--accent); display: block; }

  /* Slide 1: cover */
  .cover { top: 70px; background: var(--paper); }
  .cover .rule { height: 2px; background: var(--ink); width: 98px; left: 169px; }
  .cover .title { left: 60px; width: 316px; top: 190px; text-align: center; font-size: 48px; line-height: 57px; font-weight: 700; }
  .cover .subtitle { left: 60px; width: 316px; top: 328px; text-align: center; font-size: 26px; line-height: 37px; }

  /* Slide 2: agenda */
  .agenda { top: 753px; }
  .agenda .heading { left: 62px; top: 51px; }
  .agenda .list-box { left: 62px; top: 130px; width: 533px; height: 405px; border: 4px solid var(--panel-dark); border-top: 0; background: var(--mist); }
  .agenda .list-head { position: absolute; left: 0; top: 0; width: 100%; height: 73px; background: var(--panel-dark); color: #fff; font-size: 23px; font-weight: 700; padding: 22px 0 0 38px; }
  .agenda .list-body { position: absolute; left: 0; top: 73px; right: 0; bottom: 0; background: var(--mist); border-top: 4px solid #fff; }
  .agenda ul { list-style: none; position: absolute; left: 41px; top: 20px; width: 369px; }
  .agenda li { font-size: 24px; line-height: 71px; height: 72px; border-bottom: 1px solid var(--rule); padding-left: 1px; }
  .agenda li:last-child { border-bottom: 0; }

  /* Slide 3: problem */
  .problem { top: 1436px; background: var(--paper); }
  .problem .statement { left: 640px; width: 392px; top: 128px; text-align: center; }
  .problem .statement h2 { font-size: 38px; font-weight: 700; line-height: 44px; margin-bottom: 34px; letter-spacing: .5px; }
  .problem .statement p { font-size: 22px; line-height: 31px; }
  .problem .statement strong { color: var(--accent); font-weight: 700; }
  .problem .statement .warning { margin-top: 33px; }
  .problem .statement .warning strong { font-weight: 600; }

  /* Slide 4: what people say */
  .say { top: 2117px; }
  .say .heading { left: 83px; top: 35px; }
  .say .card { left: 83px; top: 163px; width: 831px; height: 385px; background: var(--paper); box-shadow: 0 2px 6px rgba(0,0,0,.08); }
  .say .exchange { position: absolute; left: 45px; width: 780px; font-size: 21px; line-height: 31px; color: var(--ink-soft); }
  .say .divider { position: absolute; left: 19px; width: 794px; height: 1px; background: #cfcfcf; }

  /* Slide 5: what to ask */
  .ask { top: 2798px; }
  .ask .heading { left: 55px; top: 40px; }
  .ask .col { top: 169px; width: 314px; height: 195px; background: var(--paper); box-shadow: 0 1px 4px rgba(0,0,0,.08); padding: 18px 0 0 28px; }
  .ask .col h3 { font-size: 21px; font-weight: 700; line-height: 26px; margin-bottom: 16px; }
  .ask .col--good h3 { color: var(--accent); }
  .ask .col--bad h3 { color: var(--alert); }
  .ask .col p { font-size: 16px; line-height: 20px; color: var(--ink-soft); margin-bottom: 18px; }
  .ask .tag { background: var(--accent); color: #fff; padding: 0 4px; }
  .ask .quote-box { left: 54px; top: 393px; width: 650px; height: 163px; border: 2px solid #d2d0cd; padding: 27px 0 0 30px; }
  .ask .quote-box h4 { font-size: 24px; font-weight: 700; line-height: 32px; }
  .ask .quote-box p { font-size: 24px; line-height: 34px; color: var(--ink-soft); }

  /* Slide 6: mistakes */
  .mistakes { top: 3481px; }
  .mistakes .heading { left: 59px; top: 43px; }
  .mistakes .card { left: 62px; top: 128px; width: 980px; height: 412px; background: var(--paper); box-shadow: 0 1px 4px rgba(0,0,0,.08); }
  .mistakes .card-text { position: absolute; left: 414px; top: 58px; width: 520px; }
  .mistakes h3 { font-size: 23px; font-weight: 700; line-height: 28px; }
  .mistakes .lead { font-size: 26px; line-height: 34px; margin-bottom: 22px; }
  .mistakes .note { font-size: 18px; line-height: 24px; color: var(--ink-soft); }
  .mistakes .examples { margin-top: 24px; width: 504px; height: 102px; background: var(--mist); padding: 20px 0 0 26px; font-size: 18px; line-height: 26px; font-style: italic; color: var(--ink-soft); }
</style>
</head>
<body>

<!-- Cover -->
<section class="slide cover">
  <div class="photo" role="img" aria-label="Photo: smiling businesswoman in glasses shaking hands across a desk" style="left:0;top:0;width:1098px;height:616px;background:linear-gradient(120deg,#2c2f33 0%,#4d4f52 45%,#8a8c8f 75%,#c8cbd0 100%);"></div>
  <svg style="left:0;top:0" width="1098" height="616" viewBox="0 0 1098 616" aria-hidden="true">
    <path d="M0 0 H476 C400 150 380 330 430 460 C455 540 480 590 501 616 H0 Z" fill="#ffffff"/>
  </svg>
  <div class="brand" style="left:21px;top:16px;">Zentrel</div>
  <div class="rule" style="top:158px;"></div>
  <h1 class="title">Customer Development</h1>
  <p class="subtitle">Mom’s test -<br>how to talk to customers</p>
  <div class="rule" style="top:438px;"></div>
</section>

<!-- Agenda -->
<section class="slide agenda">
  <div class="photo" role="img" aria-label="Photo: person with a backpack walking up a road toward a giant question mark under stormy clouds" style="left:527px;top:0;width:571px;height:616px;background:linear-gradient(180deg,#4a4c50 0%,#8c8f94 40%,#6e7074 70%,#2f3033 100%);"></div>
  <div class="brand brand--light" style="left:1010px;top:27px;">Zentrel</div>
  <h2 class="heading">Agenda</h2>
  <div class="list-box">
    <div class="list-head">Mom’s test:</div>
    <div class="list-body">
      <ul>
        <li>What is the problem?</li>
        <li>How to talk to customers ?</li>
        <li>How to ask questions?</li>
        <li>Who to talk to?</li>
      </ul>
    </div>
  </div>
</section>

<!-- The problem -->
<section class="slide problem">
  <svg style="left:0;top:0" width="1098" height="616" viewBox="0 0 1098 616" aria-hidden="true">
    <path d="M0 0 H535 C500 90 490 180 510 280 C530 400 560 500 512 616 H0 Z" fill="#efeeec"/>
  </svg>
  <div class="photo" role="img" aria-label="Photo: young businesswoman smiling with her hands folded under her chin" style="left:107px;top:91px;width:504px;height:380px;background:linear-gradient(135deg,#6f7478 0%,#b9b7b2 45%,#3b3a3a 75%,#8fa3ad 100%);"></div>
  <div class="brand" style="left:1000px;top:14px;">Zentrel</div>
  <div class="statement">
    <h2>THE PROBLEM</h2>
    <p>People try to be <strong>nice</strong><br>Therefore they lie in your face<br>without realizing it</p>
    <p class="warning"><strong>Bad data it worse than no data</strong><br>E.g. “I’ll definitely buy that”</p>
  </div>
</section>

<!-- What people say -->
<section class="slide say">
  <div class="photo" role="img" aria-label="Darkened photo: businesswoman in glasses shaking hands" style="left:543px;top:102px;width:555px;height:514px;background:linear-gradient(120deg,#3a3a3b 0%,#4e4d4c 55%,#6b6967 100%);"></div>
  <div class="brand" style="left:1006px;top:16px;">Zentrel</div>
  <h2 class="heading">Mom’s test&nbsp; -<span class="accent">What people say</span></h2>
  <div class="card">
    <p class="exchange" style="top:30px;">You: Mom, I have a business idea. Do you have 5 mins?<br>Mom: Of course, dear</p>
    <div class="divider" style="top:113px;"></div>
    <p class="exchange" style="top:137px;">You: You life your Orvix and use it a lot?<br>Mom: Sure it’s great</p>
    <div class="divider" style="top:219px;"></div>
    <p class="exchange" style="top:252px;">You: Would you buy a cookbook app?<br>Mom: I love cookbooks, sounds nice. Does it come with vegan recipes?<br>Or something special for Xmas?</p>
  </div>
</section>

<!-- What to ask -->
<section class="slide ask">
  <div class="brand" style="left:1006px;top:16px;">Zentrel</div>
  <h2 class="heading">What to ask?&nbsp; -<span class="accent">Important questions</span></h2>
  <div class="col col--good" style="left:55px;">
    <h3>Good</h3>
    <p>Imagine your company failed.<br>Why did it fail? → <span class="tag">Questions</span></p>
    <p>Imagine your company is<br>huge success why? → <span class="tag">Questions</span></p>
  </div>
  <div class="col col--bad" style="left:392px;">
    <h3>Bad</h3>
    <p>Deep inside, you are afraid your<br>idea might be bad</p>
    <p style="margin-top:34px;">So you ask bogus questions</p>
  </div>
  <div class="quote-box">
    <h4>Ask those questions</h4>
    <p>“ you should be terrified of at least one of the<br>questions you’re asking in every conversation”</p>
  </div>
  <div class="photo" role="img" aria-label="Photo: cheerful man in a yellow shirt talking with a woman at a table" style="left:728px;top:167px;width:345px;height:389px;background:linear-gradient(135deg,#5c4a3a 0%,#c9b9a2 35%,#d4a52a 60%,#2f3a55 100%);"></div>
</section>

<!-- Mistakes -->
<section class="slide mistakes">
  <div class="brand" style="left:1006px;top:16px;">Zentrel</div>
  <h2 class="heading">!Mistakes to avoid</h2>
  <div class="card">
    <div class="photo" role="img" aria-label="Illustration: hand holding a light bulb wearing a graduation cap, with orange rays" style="left:0;top:0;width:356px;height:412px;position:absolute;background:linear-gradient(160deg,#ececea 0%,#d8d7d4 60%,#c4b9ad 100%);"></div>
    <div class="card-text">
      <h3>EMPTY COMPLIMENTS</h3>
      <p class="lead">Don't get flattered, it won’t help your startup</p>
      <p class="note">Those are warning signal during a conversation. Direct the conversation away from you and back to the customer</p>
      <div class="examples">“ I love this!”, “ You are such a young bright student”,<br>“ this is a really good idea”</div>
    </div>
  </div>
</section>

</body>
</html>
```